Website for Sports and Exercise Medicine Doctor with active research in stem cells therapies.

I am a sports and exercise medicine doctor with research interests in the cutting edge areas of biological therapies, most notable stem cells. None of my patients are dying of anything, and most of them come to see me to decrease their pain, so they can get back to what they want to do.

The approach i then take is to decrease their pain and support them to achieve the things they wish to achieve. Most people start at "Just make it stop hurting doc" , but I try to move them towards something more important over time.

I would like the website to be very different to other "Doctor or medical websites" in its look. No pictures of doctors in white coats and no pictures of fit old people smiling. I would potentially like the fist thing seen to be a quote:

"Less pain. Everybody wants it, but what are you going to do, once you've got it?"

(But this is only an idea, I am open to anything)

The website will need a couple of things

1. "Locations" I work
2. "Research" I am involved in
3. "Sort Me out" - Clinical information for people to access
4. "Social" - imbedded chirpline and friendgrid
5. "Blog" - imbedded postmill blog
6. "Bio" - the usual bio-stuff

The "Sort Me out" - pages I would like to have the functionality as seen in this site http://www.vandrolix.com.au/platelet/. I intend to put disease topics into these pages (eg Achilles tehdinopathy, osteoarthritis etc etc etc). Once again I am not wedded to this but something along these lines would be good.

To give you an idea these are some sites I like
http://www.harborlantern.com/
http://quimbet.com/
http://orvanstudio.com.sg/
http://milbonhonestkettle.com/
http://www.tessmonthly.com/
http://gravwick.com/#offering
http://pelicanworks.tv/
http://tidalnova.com/
http://foxledger.co.uk/#about

Target Market(s)

20-80 year old.
People with tendon injuries
People with osteoarthritis
People interested in stem cells
I will build the site over time to contain information on multiple sporting injuries and musculoskeletal disorders. It will also become a site for the latest on stem cell research particularly in the area of osteoarthritis.

Industry/Entity Type

Medical

Font styles to use
Sans Serif

Colors
ffffff

Requirements
Nice to have
• To give you an idea these are some sites I like
http://quimbet.com/
http://pelicanworks.tv/
http://tidalnova.com/
Should not have
• Pictures of doctors in white coats or old fit people smiling

```html
<!DOCTYPE html>
<html lang="en">
<head>
<meta charset="utf-8">
<title>Dr. Owen Hartley — Sports and Exercise Medicine</title>
<link href="https://fonts.googleapis.com/css2?family=Open+Sans:wght@400;600&display=swap" rel="stylesheet">
<style>
:root{
  --lime:#d6df1f;
  --green:#3bb44a;
  --nav-top:#8cc640;
  --nav-bottom:#6db33f;
  --teal:#0f7a5c;
  --red:#c2202e;
  --text:#555;
  --dark:#222;
  --footer:#5b5b5b;
  --footer-text:#f0f0f0;
  --white:#fff;
  --line:#e2e2e2;
}
*{margin:0;padding:0;box-sizing:border-box}
html,body{width:1088px;height:1200px;overflow:hidden}
body{font-family:'Open Sans',sans-serif;background:var(--white);position:relative;color:var(--text)}
.abs{position:absolute}
.top-band{left:0;top:0;width:1088px;height:344px;background:var(--lime)}
.hero-wave{left:0;top:344px}
.header{left:118px;top:15px;width:852px;height:96px;background:linear-gradient(#fff,#f0f0f0)}
.brand{left:12px;top:40px;display:flex;align-items:center;gap:10px}
.brand-mark{width:36px;height:36px;border-radius:50%;background:var(--nav-top)}
.brand-name{font-size:24px;color:var(--teal);font-weight:400;letter-spacing:-.3px;white-space:nowrap}
.call{right:11px;top:27px;white-space:nowrap}
.call-label{display:flex;align-items:center;gap:8px;font-size:14px;color:var(--green)}
.call-number{font-size:24px;color:var(--red);line-height:30px;letter-spacing:.3px}
.nav{left:118px;top:119px;width:852px;height:44px;background:linear-gradient(var(--nav-top),var(--nav-bottom))}
.nav a{color:var(--white);text-decoration:none;font-size:13px;position:absolute;top:13px;white-space:nowrap}
.nav .home{left:0;top:0;width:81px;height:44px;background:linear-gradient(#128a62,#0b6850);display:flex;align-items:center;justify-content:center}
.slide{left:118px;top:169px;width:852px;height:331px;border:3px solid var(--white);background:linear-gradient(135deg,#d9d9d6,#9a9d98 55%,#5c6a5e);box-shadow:0 0 2px rgba(0,0,0,.2)}
.dots{left:498px;top:526px;display:flex;gap:6px}
.dots span{width:18px;height:18px;border-radius:50%;background:var(--white)}
.dots .on{background:var(--lime)}
h2{font-weight:400;color:var(--red);font-size:19px;white-space:nowrap}
p.body{font-size:12px;line-height:21px;color:var(--text)}
.welcome{left:119px;top:601px;width:480px}
.welcome p{margin-top:8px}
.btn{left:118px;top:743px;width:100px;height:34px;background:var(--green);color:var(--white);font-size:12px;display:flex;align-items:center;justify-content:center}
.more{font-size:12px;color:var(--dark);font-weight:600;letter-spacing:.2px}
.news{left:626px;top:602px;width:344px;height:174px;border:1px solid var(--line);background:linear-gradient(#f3f3f3,#fff);padding:12px 20px}
.news .date{font-size:12px;color:var(--green);font-weight:600;margin-top:12px}
.news p{margin-top:2px}
.news .more{display:block;margin-top:9px}
.squares{left:285px;top:20px;display:flex;gap:6px}
.squares span{width:11px;height:11px;background:#aaa}
.squares .on{background:var(--nav-top)}
.research-bg{left:118px;top:804px;width:852px;height:200px;border-top:1px solid var(--line);background:linear-gradient(#f2f2f2,#fff)}
.research-title{left:139px;top:821px}
.research-photo{left:140px;top:863px;width:174px;height:129px;background:linear-gradient(135deg,#e7ecef,#b7c3cc 50%,#6f8ca8)}
.research-text{left:336px;top:857px;width:336px}
.research-text .more{display:block;margin-top:10px}
.blog{left:697px;top:824px;width:260px;height:168px;border:1px solid var(--line);background:var(--white);padding:12px 18px;box-shadow:0 8px 8px -6px rgba(0,0,0,.12)}
.blog-thumb{left:18px;top:50px;width:47px;height:47px;background:linear-gradient(135deg,#9fb6c8,#5d7591)}
.blog-entry{left:81px;top:47px;width:165px}
.blog-entry h3{font-size:12px;color:var(--green);font-weight:600;white-space:nowrap}
.blog-entry p{margin-top:2px}
.blog-entry .more{display:block;margin-top:7px}
.footer{left:0;top:1033px;width:1088px;height:167px;background:var(--footer)}
.footer h4{font-size:15px;color:var(--lime);font-weight:400;position:absolute;top:20px}
.footer a{font-size:11.5px;color:var(--footer-text);text-decoration:none;position:absolute;white-space:nowrap}
.social-icon{position:absolute;width:14px;height:14px;background:#8aa2c0;border-radius:2px}
.foot-brand{right:118px;top:1060px;display:flex;flex-direction:column;align-items:center;gap:6px}
.foot-brand .brand-mark{width:40px;height:40px}
.foot-brand .brand-name{font-size:21px;color:var(--white)}
.copy{right:118px;top:1150px;text-align:right;font-size:11px;line-height:18px;color:#d8d8d8;white-space:nowrap}
.copy span{color:var(--lime)}
</style>
</head>
<body>
<div class="abs top-band"></div>
<svg class="abs hero-wave" width="1088" height="230" viewBox="0 0 1088 230">
  <path d="M0 0 H1088 V141 Q544 309 0 141 Z" fill="#3bb44a"/>
</svg>

<header class="abs header">
  <div class="abs brand"><span class="brand-mark"></span><span class="brand-name">Dr.Owen Hartley</span></div>
  <div class="abs call">
    <div class="call-label">
      <svg width="14" height="14" viewBox="0 0 14 14"><rect width="14" height="14" rx="2" fill="#666"/><path d="M4 3 L6 3 L6.5 5.5 L5.3 6.3 Q6.3 8.4 8 9 L8.7 7.8 L11 8.3 L11 10.5 Q6 11 3.5 5 Z" fill="#fff"/></svg>
      Call Us:
    </div>
    <div class="call-number">121 555 0188</div>
  </div>
</header>

<nav class="abs nav">
  <a class="home" href="#">HOME</a>
  <a href="#" style="left:92px">LOCATIONS</a>
  <a href="#" style="left:196px">RESEARCH</a>
  <a href="#" style="left:292px">SORT ME OUT</a>
  <a href="#" style="left:410px">SOCIAL</a>
  <a href="#" style="left:487px">BLOG</a>
  <a href="#" style="left:554px">BIO</a>
  <a href="#" style="left:609px">CONTACT US</a>
</nav>

<div class="abs slide" role="img" aria-label="Exercise lab: a patient on a treadmill wearing a breathing mask during a fitness test, with clinicians watching monitors"></div>
<div class="abs dots"><span class="on"></span><span></span><span></span><span></span></div>

<section class="abs welcome">
  <h2>Welcome to Our Website</h2>
  <p class="body">Aliquam nibh ante, egestas id dictum a, commodo luctus libero. Praesent faucibus malesuada faucibus. Donecyl laoreet metus id laoreet malesuada. Lorem ipsum dolor sit amet, consectetur adipiscing elit. Nullam consectetu orci sed nulla facilisis consequat. Curabitur vel lorem sit amet nulla ullamcorper fermentum.</p>
</section>
<a class="abs btn">READ MORE</a>

<aside class="abs news">
  <h2>Latest News</h2>
  <div class="abs squares"><span class="on"></span><span></span><span></span></div>
  <div class="date">DEC 10, 2013</div>
  <p class="body">Aliquam nibh ante, egestas id dictum a, commodo luctus libero. Praesent faucibus malesuada faucibus. Donecy laoreet metus id laoreet malesuada...</p>
  <span class="more">READ MORE</span>
</aside>

<div class="abs research-bg"></div>
<h2 class="abs research-title">Our Research</h2>
<div class="abs research-photo" role="img" aria-label="Researcher in a laboratory working with a pipette"></div>
<div class="abs research-text">
  <p class="body">Aliquam nibh ante, egestas id dictum a, commodo luctus libero. Praesent faucibus malesuada faucibus. Donecyl laoreet metus id laoreet malesuada. Lorem ipsum dolor sit amet, consectetur adipiscing elit. Nullam consectetu orci sed nulla facilisis consequat.</p>
  <span class="more">READ MORE</span>
</div>

<aside class="abs blog">
  <h2>Blog Posts</h2>
  <div class="abs blog-thumb" role="img" aria-label="Blog post thumbnail of an office scene"></div>
  <div class="abs blog-entry">
    <h3>Setrolis assa elit, auctor</h3>
    <p class="body">Aliquam nibh ante, egestas id dictum a, commodo luctus libero.</p>
    <span class="more">READ MORE</span>
  </div>
</aside>

<footer class="abs footer">
  <h4 style="left:118px">Quick Links</h4>
  <a style="left:118px;top:57px">Home</a>
  <a style="left:118px;top:84px">Locations</a>
  <a style="left:118px;top:110px">Research</a>
  <a style="left:118px;top:136px">Sort me Out</a>
  <a style="left:228px;top:57px">Social</a>
  <a style="left:228px;top:84px">Blog</a>
  <a style="left:228px;top:110px">Bio</a>

  <h4 style="left:325px">Locations</h4>
  <a style="left:325px;top:57px">Setrolis assa elit</a>
  <a style="left:325px;top:84px">Master lam eget</a>
  <a style="left:325px;top:110px">Do nisi nibh ut semper</a>
  <a style="left:325px;top:136px">Sertloque</a>

  <h4 style="left:500px">Connect Us</h4>
  <span class="social-icon" style="left:501px;top:59px"></span><a style="left:528px;top:57px">Friendgrid</a>
  <span class="social-icon" style="left:501px;top:86px;background:#9cc8dd"></span><a style="left:528px;top:84px">Chirpline</a>
  <span class="social-icon" style="left:501px;top:112px;background:#7ea6c4"></span><a style="left:528px;top:110px">LinkNest</a>
  <span class="social-icon" style="left:501px;top:138px;background:#e98a2e"></span><a style="left:528px;top:136px">Rss Feeds</a>
</footer>
<div class="abs foot-brand"><span class="brand-mark"></span><span class="brand-name">Dr.Owen Hartley</span></div>
<div class="abs copy">Copyright © 2013 <span>Dr.Owen Hartley</span><br>All Right Reserved</div>
</body>
</html>
```